K&T Fixit and Rebuild general contracting business card design

I already have a logo that I want to use and I need a card that uses that logo and color scheme on the front with the address phone numbers and email and on the back a place for technicians to write in their name and phone number when they hand it out. It will need the License number of License #KTFXTRB318QN.
It should say General Contractor under the company name. The address is
4417 NE 3rd Ave, Ste D246
Vancouver, WA 98612
www.kandtfixitandrebuild.example
office@kandtfixitandrebuild.example
360-555-0182 is the telephone number
360-555-0149 is the fax number

Target Market(s)

Homeowners needing remodel work or repairs in their home.

Industry/Entity Type

Construction

Contact Information for Business Card

Business name, address, phone number, license number, fax number, email, and website on the front and a place to fill in technician's name and number

Font styles to use
Serif

Requirements
Must have
• Business name, address, phone number, license number, fax number, email, and website on the front and a place to fill in technician's name and number
Nice to have
• I uploaded an example of a front that is good.
Should not have
• Froo froo or extra embellishments.

```html
<!DOCTYPE html>
<html lang="en">
<head>
<meta charset="utf-8">
<title>K&amp;T Fixit and Rebuild — Business Cards</title>
<link href="https://fonts.googleapis.com/css2?family=Cinzel:wght@600&family=Lora:wght@400;700&display=swap" rel="stylesheet">
<style>
  :root {
    --stage: #1b1b1b;
    --wood-dark: #2a160c;
    --wood-mid: #5a3019;
    --wood-light: #7a4325;
    --copper: #c97d52;
    --ink-light: #ffffff;
    --band: #ffffff;
    --band-ink: #2b2b2b;
    --rule: #8a8a8a;
  }
  * { box-sizing: border-box; margin: 0; padding: 0; }
  html, body {
    width: 1200px; height: 900px; overflow: hidden;
    background: var(--stage);
  }
  .stage {
    width: 1200px; height: 900px;
    display: flex; flex-direction: column; align-items: center; justify-content: center;
    gap: 50px;
  }
  .card {
    position: relative;
    width: 630px; height: 360px;
    overflow: hidden;
    box-shadow: 0 12px 30px rgba(0,0,0,.6);
  }
  .card__wood {
    position: absolute; inset: 0;
    background: radial-gradient(ellipse at 55% 40%, var(--wood-light) 0%, var(--wood-mid) 45%, var(--wood-dark) 100%);
  }
  .brand {
    position: absolute; left: 0; right: 0;
    text-align: center;
    font-family: "Cinzel", serif;
    font-weight: 600;
    letter-spacing: 1px;
  }
  .brand__name { font-size: 28px; line-height: 1.2; }
  .brand__tag { font-size: 18px; margin-top: 8px; letter-spacing: 2px; }

  /* back card */
  .card--back .brand { top: 70px; color: var(--copper); }
  .card--back .brand__tag { color: var(--ink-light); }
  .fill-band {
    position: absolute; left: 0; right: 0; bottom: 0; height: 130px;
    background: var(--band);
    padding: 30px 60px 0 80px;
    font-family: "Lora", serif;
    font-size: 17px; color: var(--band-ink);
  }
  .fill-band__row { display: flex; align-items: flex-end; gap: 16px; height: 40px; }
  .fill-band__label { width: 80px; }
  .fill-band__line { flex: 1; border-bottom: 1px solid var(--rule); height: 1px; margin-bottom: 4px; }

  /* front card */
  .card--front .brand { top: 78px; color: var(--ink-light); }
  .contact {
    position: absolute; left: 0; right: 0; top: 150px;
    text-align: center;
    font-family: "Lora", serif;
    color: var(--ink-light);
    font-size: 17px; line-height: 1.55;
  }
  .contact b { font-weight: 700; }
  .contact__sep { padding: 0 10px; }
  .contact__rule { width: 90px; margin: 4px auto; border-top: 1px solid rgba(255,255,255,.5); }
  .contact__license { font-size: 14px; letter-spacing: .5px; margin-top: 2px; }
</style>
</head>
<body>
<main class="stage">
  <section class="card card--back">
    <div class="card__wood" role="img" aria-label="Dark stained wood plank texture"></div>
    <div class="brand">
      <div class="brand__name">K&amp;T Fixit and Rebuild</div>
      <div class="brand__tag">GENERAL CONTRACTOR</div>
    </div>
    <div class="fill-band">
      <div class="fill-band__row"><span class="fill-band__label">Name:</span><span class="fill-band__line"></span></div>
      <div class="fill-band__row"><span class="fill-band__label">Contact:</span><span class="fill-band__line"></span></div>
    </div>
  </section>

  <section class="card card--front">
    <div class="card__wood" role="img" aria-label="Warm brown wood plank texture"></div>
    <div class="brand">
      <div class="brand__name">K&amp;T Fixit and Rebuild</div>
    </div>
    <div class="contact">
      <p><b>P:</b> 360-555-0182<span class="contact__sep">|</span><b>F:</b> 360-555-0149</p>
      <p>office@kandtfixitandrebuild.example</p>
      <p>www.kandtfixitandrebuild.example</p>
      <div class="contact__rule"></div>
      <p>4417 NE 3rd Ave, Ste D246 Vancouver, WA 98612</p>
      <p class="contact__license">License #KTFXTRB318QN</p>
    </div>
  </section>
</main>
</body>
</html>
```